hi all

Im after a new age looking business card with my company logo on it

must include these details, I would like the PH and Email to be symbols

If the colours used for card could be kept within the colours used in logo that I have supplied that would be great, if another colour is to be used dark grey would be ok. no light bulbs etc thanks

Details below to be incorporated on card

Damian Holloway

Lic E871302

PH 0219647381

E info@brightvaleelectrical.example.nz

Domestic Commercial Industrial Electricians

```html
<!DOCTYPE html>
<html lang="en">
<head>
<meta charset="utf-8">
<title>Brightvale Electrical – Business Card</title>
<link rel="stylesheet" href="https://fonts.googleapis.com/css2?family=Montserrat:wght@400;500;700;800&display=swap">
<style>
  :root {
    --brand-blue: #0b63ad;
    --brand-blue-deep: #08548f;
    --ink: #2b2b2b;
    --card-white: #ffffff;
    --band-silver: #d9dde2;
    --band-silver-dark: #aab2bb;
    --stage: #e9eaec;
  }
  * { box-sizing: border-box; margin: 0; padding: 0; }
  html, body {
    width: 1200px; height: 922px; overflow: hidden;
    background: var(--stage);
    font-family: "Montserrat", sans-serif;
  }
  .canvas {
    position: relative; width: 1200px; height: 922px;
    display: flex; align-items: center; justify-content: center; gap: 48px;
  }
  .card {
    position: relative; width: 500px; height: 286px;
    border-radius: 4px; overflow: hidden;
    box-shadow: 0 8px 24px rgba(0,0,0,.18);
  }

  /* Front */
  .card-front { background: var(--brand-blue); }
  .front-texture {
    position: absolute; inset: 0;
    background: radial-gradient(circle at 62% 40%, rgba(255,255,255,.10), rgba(255,255,255,0) 60%);
  }
  .front-wordmark {
    position: absolute; left: 0; right: 0; top: 78px;
    display: flex; flex-direction: column; align-items: center; gap: 8px;
    color: var(--card-white);
  }
  .front-wordmark .mark-dot {
    width: 22px; height: 22px; border-radius: 50%; background: var(--card-white);
  }
  .front-wordmark .name {
    font-weight: 800; font-size: 38px; letter-spacing: 3px; text-transform: uppercase;
  }
  .front-wordmark .sub {
    font-weight: 800; font-size: 15px; letter-spacing: 8px; text-transform: uppercase;
  }
  .services-band {
    position: absolute; left: 0; right: 0; bottom: 0; height: 30px;
    background: linear-gradient(90deg, var(--band-silver-dark), var(--band-silver) 30%, var(--band-silver) 70%, var(--band-silver-dark));
    display: flex; align-items: center; justify-content: center;
    color: var(--brand-blue-deep); font-size: 11px; font-weight: 500;
    letter-spacing: 1.6px; text-transform: uppercase;
  }

  /* Back */
  .card-back { background: var(--card-white); border-bottom: 4px solid var(--brand-blue); }
  .contact {
    position: absolute; left: 34px; top: 68px; color: var(--ink);
  }
  .contact .person {
    color: var(--brand-blue); font-weight: 800; font-size: 15px;
    letter-spacing: 1px; text-transform: uppercase;
  }
  .contact .licence { font-size: 13px; margin-top: 4px; }
  .contact .rule { width: 16px; height: 2px; background: var(--brand-blue); margin: 12px 0 14px; }
  .contact .line { display: flex; align-items: center; gap: 8px; font-size: 13px; margin-bottom: 8px; }
  .contact svg { width: 13px; height: 13px; fill: none; stroke: var(--brand-blue); stroke-width: 2; }
  .back-wordmark {
    position: absolute; right: 30px; top: 78px; text-align: right;
    color: var(--brand-blue); display: flex; flex-direction: column; align-items: flex-end; gap: 5px;
  }
  .back-wordmark .mark-dot { width: 16px; height: 16px; border-radius: 50%; background: var(--brand-blue); align-self: center; }
  .back-wordmark .name { font-weight: 800; font-size: 24px; letter-spacing: 2px; text-transform: uppercase; }
  .back-wordmark .sub { font-weight: 800; font-size: 10px; letter-spacing: 5px; text-transform: uppercase; }
</style>
</head>
<body>
<main class="canvas">
  <section class="card card-front" aria-label="Card front">
    <div class="front-texture" role="img" aria-label="Faint circuit-line backdrop in blue tones"></div>
    <div class="front-wordmark">
      <span class="mark-dot"></span>
      <span class="name">Brightvale</span>
      <span class="sub">Electrical</span>
    </div>
    <div class="services-band">Domestic • Commercial • Industrial • Electricians</div>
  </section>

  <section class="card card-back" aria-label="Card back">
    <div class="contact">
      <p class="person">Damian Holloway</p>
      <p class="licence">Lic E871302</p>
      <div class="rule"></div>
      <p class="line">
        <svg viewBox="0 0 24 24" aria-hidden="true"><path d="M5 3h4l2 5-3 2a12 12 0 0 0 6 6l2-3 5 2v4a2 2 0 0 1-2 2A17 17 0 0 1 3 5a2 2 0 0 1 2-2z"/></svg>
        021 964 7381
      </p>
      <p class="line">
        <svg viewBox="0 0 24 24" aria-hidden="true"><rect x="3" y="5" width="18" height="14" rx="2"/><path d="M3 7l9 6 9-6"/></svg>
        info@brightvaleelectrical.example.nz
      </p>
    </div>
    <div class="back-wordmark">
      <span class="mark-dot"></span>
      <span class="name">Brightvale</span>
      <span class="sub">Electrical</span>
    </div>
  </section>
</main>
</body>
</html>
```